Carpet Cleaning & Car Detailing. I don't have a logo design yet. I like electric blue black and white as the colours.

We clean:

- Carpets
- rugs

We have added the car detailing to the bussiness

- car detailing
- seat cleaning
- carpet cleaning

Carpet

movercarpetcleaning@quellmail.net
0491 826 073

```html
<!DOCTYPE html>
<html lang="en">
<head>
<meta charset="utf-8">
<title>Mover Carpet Cleaning – Business Card</title>
<link rel="stylesheet" href="https://fonts.googleapis.com/css2?family=Archivo:wdth,wght@100..125,700;100..125,800&family=Arimo:wght@700&display=swap">
<style>
  :root {
    --card-black: #231f20;
    --electric-blue: #3a64b4;
    --brand-blue: #4f74c9;
    --text-white: #ffffff;
  }
  html, body {
    margin: 0;
    padding: 0;
    width: 1200px;
    height: 739px;
    overflow: hidden;
    background: var(--card-black);
  }
  .business-card {
    display: block;
    width: 1200px;
    height: 739px;
  }
  .card-frame {
    fill: none;
    stroke: var(--electric-blue);
    stroke-width: 3;
  }
  .brand-name {
    font-family: "Arimo", Arial, sans-serif;
    font-weight: 700;
    fill: var(--brand-blue);
  }
  .brand-tagline {
    font-family: "Arimo", Arial, sans-serif;
    font-weight: 700;
    fill: var(--text-white);
  }
  .contact-phone {
    font-family: "Archivo", Arial, sans-serif;
    font-weight: 800;
    font-stretch: 125%;
    fill: var(--text-white);
  }
  .contact-email {
    font-family: "Arimo", Arial, sans-serif;
    font-weight: 700;
    fill: var(--text-white);
  }
  .service-item {
    font-family: "Archivo", Arial, sans-serif;
    font-weight: 800;
    font-stretch: 115%;
    fill: var(--text-white);
  }
</style>
</head>
<body>
<svg class="business-card" viewBox="0 0 1200 739" xmlns="http://www.w3.org/2000/svg" role="img" aria-label="Mover Carpet Cleaning business card">
  <rect class="card-background" x="0" y="0" width="1200" height="739" fill="var(--card-black)"/>
  <rect class="card-frame" x="60" y="60" width="1082" height="625"/>

  <text class="brand-name" x="130" y="360" font-size="330" textLength="960" lengthAdjust="spacingAndGlyphs">Mover</text>
  <text class="brand-tagline" x="395" y="443" font-size="66" textLength="630" lengthAdjust="spacingAndGlyphs">Carpet Cleaning</text>

  <text class="contact-phone" x="113" y="581" font-size="56" textLength="566" lengthAdjust="spacingAndGlyphs">0491 826 073</text>
  <text class="contact-email" x="116" y="636" font-size="26" textLength="563" lengthAdjust="spacingAndGlyphs">movercarpetcleaning@quellmail.net</text>

  <g class="service-list">
    <text class="service-item" x="746" y="538" font-size="32" textLength="292" lengthAdjust="spacingAndGlyphs">Car Detailing</text>
    <text class="service-item" x="746" y="587" font-size="32" textLength="313" lengthAdjust="spacingAndGlyphs">Seat Cleaning</text>
    <text class="service-item" x="746" y="636" font-size="32" textLength="362" lengthAdjust="spacingAndGlyphs">Carpet Cleaning</text>
  </g>
</svg>
</body>
</html>
```